Marlow Realty Real Estate Brokerage Recruiting Flyer

We are a real estate brokerage looking to hire more real estate agents. We need to list everything we have to offer as a company so real estate agents will join our company. this is our company website: www.Marlowrealty.example .

100% COMMISSION NO MONTHLY FEE
$450 Flat Transaction FEE

What We Offer:
24/7 Office Access
Free E & O Insurance for 1st Year
Free Online CE and PLE
Free 1,000 Business Cards
Free Professional Social Media Marketing
Free Printing, Scanning, and Copies
Free Buyer and Seller Presentation Packages
Free Filquay Cloud Based Document Management Access
Access to our Internal Brokerage Forum
Company Profit Sharing!
Private Offices Available to Rent

*Lead Generation Software with over 3,000 Leads
*10 Leads to Start
* Free Personal CRM and Website
*Restrictions and Rules apply

Company Address:
4817 Amberfield Road
Suite 512
Fairfax, VA 22194
Phone: 703-555-0147
email: info@marlowrealty.example

Target Market(s)

Real Estate Agents

Industry/Entity Type

Real Estate

Colors
0555a3
ffffff

Requirements
Must have
• 100% COMMISSION NO MONTHLY FEE
$450 Flat Transaction FEE

What We Offer:
24/7 Office Access
Free Online CE and PLE
Free 1,000 Business Cards
Company Profit Sharing!

*10 Leads to Start

Company Address:
4817 Amberfield Road
Suite 512
Fairfax, VA 22194
Phone: 703-555-0147

```html
<!DOCTYPE html>
<html lang="en">
<head>
<meta charset="utf-8">
<title>Marlow Realty – Agent Recruiting Flyer</title>
<link rel="stylesheet" href="https://fonts.googleapis.com/css2?family=Montserrat:wght@400;800&family=Questrial&family=Roboto+Condensed:wght@400;700&display=swap">
<style>
  :root {
    --navy: #1d3a78;
    --navy-deep: #0f2450;
    --navy-stripe: #26478a;
    --white: #ffffff;
    --grey: #d4d5d9;
    --ink: #1d3a78;
  }
  * { box-sizing: border-box; margin: 0; padding: 0; }
  html, body { width: 927px; height: 1200px; overflow: hidden; background: var(--white); }
  .flyer { position: relative; width: 927px; height: 1200px; overflow: hidden; background: var(--white); font-family: "Roboto Condensed", sans-serif; color: var(--ink); }
  .hero-art { position: absolute; left: 0; top: 0; }

  .contact-top { position: absolute; right: 412px; top: 40px; text-align: right; color: var(--ink); }
  .contact-top .line { display: flex; align-items: center; justify-content: flex-end; gap: 10px; }
  .contact-top .email { font-size: 22px; font-weight: 400; height: 30px; }
  .contact-top .phone { font-size: 24px; font-weight: 700; height: 32px; }
  .divider-top { position: absolute; left: 579px; top: 49px; width: 2px; height: 56px; background: var(--navy); }
  .brand { position: absolute; left: 640px; top: 58px; display: flex; align-items: center; gap: 10px; font-family: "Questrial", sans-serif; font-size: 31px; color: var(--navy); }
  .brand .mark { width: 22px; height: 22px; background: var(--navy); }

  .headline { position: absolute; left: 28px; top: 232px; color: var(--white); font-family: "Montserrat", sans-serif; }
  .headline .commission { font-size: 40px; font-weight: 400; line-height: 46px; letter-spacing: 0.5px; }
  .headline .no-fee { font-size: 41px; font-weight: 800; line-height: 48px; }
  .fee-tag { position: absolute; left: 28px; top: 329px; width: 383px; height: 31px; background: var(--white); color: var(--navy); font-family: "Questrial", sans-serif; font-size: 24px; letter-spacing: 3px; line-height: 31px; text-align: center; }

  .offer-title { position: absolute; left: 29px; top: 582px; width: 225px; height: 45px; background: var(--navy); border-bottom: 4px solid #c9ccd3; color: var(--white); font-family: "Questrial", sans-serif; font-size: 26px; line-height: 42px; text-align: center; }

  .offer-list { position: absolute; list-style: none; font-size: 19px; line-height: 33.3px; color: #1a2340; }
  .offer-list.left { left: 28px; top: 648px; }
  .offer-list.right { left: 525px; top: 648px; }
  .offer-list li { display: flex; align-items: flex-start; }
  .offer-list .tick { width: 15px; height: 15px; margin: 9px 17px 0 0; flex: none; }
  .offer-list.right .tick { margin-right: 11px; }

  .perks { position: absolute; left: 0; top: 876px; width: 927px; height: 229px; background: linear-gradient(110deg, #23427f 0%, #2c4b88 45%, #203d78 100%); }
  .perks .perk { position: absolute; top: 36px; width: 220px; margin-left: -110px; text-align: center; color: var(--white); font-family: "Questrial", sans-serif; font-size: 19px; line-height: 23.5px; }
  .perks .perk svg { display: block; margin: 0 auto 15px; }
  .perks .sep { position: absolute; top: 47px; height: 66px; border-left: 1px dashed rgba(255,255,255,0.55); }

  .footer { position: absolute; left: 0; top: 1105px; width: 927px; height: 95px; background: var(--grey); }
  .address-tab { position: absolute; left: 356px; top: 1085px; width: 213px; height: 43px; }
  .address-tab span { position: absolute; inset: 0; text-align: center; font-family: "Questrial", sans-serif; font-size: 25px; line-height: 43px; color: var(--navy); }
  .footer-row { position: absolute; left: 30px; right: 26px; top: 1148px; display: flex; align-items: center; justify-content: space-between; color: var(--navy); font-weight: 700; font-size: 16px; }
  .footer-row .item { display: flex; align-items: center; gap: 8px; }
  .footer-row .phone { font-size: 22px; }
  .footer-row .bar { font-weight: 400; font-size: 20px; }
</style>
</head>
<body>
<div class="flyer">

  <svg class="hero-art" width="927" height="640" viewBox="0 0 927 640">
    <defs>
      <linearGradient id="photoTone" x1="0" y1="0" x2="1" y2="1">
        <stop offset="0" stop-color="#1a2f5c"/>
        <stop offset="0.55" stop-color="#2a3f66"/>
        <stop offset="1" stop-color="#17284d"/>
      </linearGradient>
    </defs>
    <path d="M0,40 H927 V520 L0,500 Z" fill="var(--navy-stripe)"/>
    <path d="M0,72 C420,175 690,195 927,138 V520 L0,500 Z" fill="var(--navy-deep)"/>
    <g role="img" aria-label="Photo of an agent in a suit holding a model house on his palm">
      <rect x="393" y="167" width="534" height="345" fill="url(#photoTone)"/>
    </g>
    <path d="M0,484 C300,462 650,470 927,520 L927,548 L800,618 C620,540 350,495 0,498 Z" fill="var(--navy)"/>
    <path d="M0,498 C350,495 620,540 800,618 L927,548 V640 H0 Z" fill="var(--white)"/>
    <path d="M0,0 H927 V124 C700,178 430,160 0,49 Z" fill="var(--white)"/>
  </svg>

  <div class="contact-top">
    <div class="line email">info@marlowrealty.example
      <svg width="18" height="14" viewBox="0 0 18 14"><rect x="0" y="0" width="18" height="14" rx="1.5" fill="var(--navy)"/><path d="M1,1.5 L9,7.5 L17,1.5" stroke="#fff" stroke-width="1.6" fill="none"/></svg>
    </div>
    <div class="line phone">703-555-0147
      <svg width="18" height="18" viewBox="0 0 24 24"><path d="M6.6 10.8a15.1 15.1 0 0 0 6.6 6.6l2.2-2.2c.3-.3.7-.4 1-.2 1.1.4 2.3.6 3.6.6.6 0 1 .4 1 1V20c0 .6-.4 1-1 1C10.6 21 3 13.4 3 4c0-.6.4-1 1-1h3.5c.6 0 1 .4 1 1 0 1.3.2 2.5.6 3.6.1.3 0 .7-.2 1z" fill="var(--navy)"/></svg>
    </div>
  </div>
  <div class="divider-top"></div>
  <div class="brand"><span class="mark"></span>Marlow Realty</div>

  <div class="headline">
    <div class="commission">100% COMMISSION</div>
    <div class="no-fee">NO MONTHLY FEE</div>
  </div>
  <div class="fee-tag">$450 Flat Transaction Fee</div>

  <div class="offer-title">What We Offer</div>

  <svg width="0" height="0" style="position:absolute">
    <symbol id="tick" viewBox="0 0 16 16"><rect x="1" y="2" width="12" height="12" rx="2" fill="none" stroke="var(--navy)" stroke-width="1.8"/><path d="M4.5 7.5 L7.5 10.5 L15 2.5" fill="none" stroke="var(--navy)" stroke-width="2"/></symbol>
  </svg>

  <ul class="offer-list left">
    <li><svg class="tick"><use href="#tick"/></svg>24/7 Office Access</li>
    <li><svg class="tick"><use href="#tick"/></svg>Free E &amp; O Insurance for 1st Year</li>
    <li><svg class="tick"><use href="#tick"/></svg>Free Online CE and PLE</li>
    <li><svg class="tick"><use href="#tick"/></svg>Free 1,000 Business Cards</li>
    <li><svg class="tick"><use href="#tick"/></svg>Free Professional Social Media Marketing</li>
    <li><svg class="tick"><use href="#tick"/></svg>Free Printing, Scanning, and Copies</li>
  </ul>
  <ul class="offer-list right">
    <li><svg class="tick"><use href="#tick"/></svg>Free Buyer and Seller Presentation Packages</li>
    <li><svg class="tick"><use href="#tick"/></svg><span>Free Filquay Cloud Based Document<br>Management Access</span></li>
    <li><svg class="tick"><use href="#tick"/></svg>Access to our Internal Brokerage Forum</li>
    <li><svg class="tick"><use href="#tick"/></svg>Company Profit Sharing!</li>
    <li><svg class="tick"><use href="#tick"/></svg>Private Offices Available to Rent</li>
  </ul>

  <section class="perks">
    <div class="perk" style="left:116px">
      <svg width="70" height="70" viewBox="0 0 70 70" fill="none" stroke="#fff" stroke-width="2"><path d="M14 26 L24 14 H46 L56 26 L35 56 Z"/><path d="M14 26 H56 M24 14 L30 26 L35 56 M46 14 L40 26 L35 56"/><circle cx="46" cy="44" r="9" fill="#2a4a88"/><path d="M52.5 50.5 L60 58"/></svg>
      Lead Generation<br>Software with over<br>3,000 Leads
    </div>
    <span class="sep" style="left:248px"></span>
    <div class="perk" style="left:356px">
      <svg width="70" height="70" viewBox="0 0 70 70" fill="none" stroke="#fff" stroke-width="2"><path d="M35 4 C46 14 46 32 43 46 H27 C24 32 24 14 35 4 Z"/><path d="M27 34 L20 48 L27 46 M43 34 L50 48 L43 46"/><path d="M31 52 V58 M35 52 V64 M39 52 V58"/><path d="M33 24 V30 M37 22 V30"/></svg>
      10 Leads to<br>Start
    </div>
    <span class="sep" style="left:457px"></span>
    <div class="perk" style="left:574px">
      <svg width="70" height="70" viewBox="0 0 70 70" fill="none" stroke="#fff" stroke-width="2"><rect x="8" y="6" width="54" height="56" rx="2"/><path d="M8 16 H62"/><rect x="12" y="9" width="4" height="4"/><rect x="19" y="9" width="4" height="4"/><rect x="26" y="9" width="4" height="4"/><path d="M20 40 A15 15 0 0 1 50 40"/><path d="M8 44 H62"/><text x="35" y="58" text-anchor="middle" fill="#fff" stroke="none" font-family="Questrial, sans-serif" font-size="13" letter-spacing="2">CRM</text></svg>
      Free Personal CRM<br>and Website
    </div>
    <span class="sep" style="left:706px"></span>
    <div class="perk" style="left:829px">
      <svg width="70" height="70" viewBox="0 0 70 70" fill="none" stroke="#fff" stroke-width="2"><circle cx="35" cy="28" r="18"/><path d="M28 20 V36 M35 20 V36 M42 20 V36"/><circle cx="28" cy="25" r="2.5"/><circle cx="35" cy="31" r="2.5"/><circle cx="42" cy="26" r="2.5"/><circle cx="17" cy="12" r="6" fill="#2a4a88"/><circle cx="54" cy="40" r="6" fill="#2a4a88"/><rect x="26" y="52" width="18" height="12"/><path d="M35 46 V52 M20 58 H26 M44 58 H50"/></svg>
      Restrictions and<br>Rules apply
    </div>
  </section>

  <footer class="footer"></footer>
  <svg class="address-tab" width="213" height="43" viewBox="0 0 213 43"><path d="M16 0 H197 L213 21.5 L197 43 H16 L0 21.5 Z" fill="var(--white)"/></svg>
  <div class="address-tab"><span>Address</span></div>

  <div class="footer-row">
    <div class="item">
      <svg width="14" height="19" viewBox="0 0 14 19"><path d="M7 0a7 7 0 0 0-7 7c0 5 7 12 7 12s7-7 7-12a7 7 0 0 0-7-7zm0 9.5A2.5 2.5 0 1 1 7 4.5a2.5 2.5 0 0 1 0 5z" fill="var(--navy)"/></svg>
      4817 Amberfield Road, Suite 512, Fairfax, VA 22194
    </div>
    <span class="bar">|</span>
    <div class="item phone">
      <svg width="18" height="18" viewBox="0 0 24 24"><path d="M6.6 10.8a15.1 15.1 0 0 0 6.6 6.6l2.2-2.2c.3-.3.7-.4 1-.2 1.1.4 2.3.6 3.6.6.6 0 1 .4 1 1V20c0 .6-.4 1-1 1C10.6 21 3 13.4 3 4c0-.6.4-1 1-1h3.5c.6 0 1 .4 1 1 0 1.3.2 2.5.6 3.6.1.3 0 .7-.2 1z" fill="var(--navy)"/></svg>
      703-555-0147
    </div>
    <span class="bar">|</span>
    <div class="item">
      <svg width="18" height="14" viewBox="0 0 18 14"><rect width="18" height="14" rx="1.5" fill="var(--navy)"/><path d="M1,1.5 L9,7.5 L17,1.5" stroke="#d4d5d9" stroke-width="1.6" fill="none"/></svg>
      info@marlowrealty.example
    </div>
  </div>

</div>
</body>
</html>
```